New Packaging Design Project for a Magnetic Toy

Hi guys, we are looking to create a packaging design for our new magnetic fidget toy called Zentrolix. Please see attached the dye cut of the box (File 1)
Top of the outer sleeve
Logo (File 2)
On the front of the box, we want you to include the following:
Logo (file 2)
Main picture of the product (File 3)
Include the phrase: “Magnetic fidget pyramids.”
Include our Slogan: “Let your creativity run wild.”
For the right side of the outer sleeve of the box please include the following:
- What’s included in the box:
o 3D image of a Tetrahedron (4) please see the picture attached file 5 as a reference to make the 3D figure and specify quantity “4”
o 3D image of 1 Tripyramidal (16) please see the picture attached file 4 as a reference to make the 3D figure and specify quantity “16”
o Storage bag. please see the picture attached (file 6)
o Stater guide. please see the picture attached (file 7) Please use file 7 as a reference you need to recreate that image using our logo.
Type the phrase “Limitless designs for Limitless minds.”
For the left side of the outer sleeve of the box please include the following:
80 powerful magnets
Picture (2-piece file 8) +
Type the phrase: Magnetic Fidget Pyramids
Warning label (File 9)
For the back side of the outer sleeve of the box:
Insert our logo (file 2)
Type the phrase: Make your 3D figures come to life!
• Square (file 10)
• Crab (file 11)
• Snake (file 12)
• Brickora (file 13)
Inner box
Top of the inner box:
Warning label
Left and right sides of the inner box
Logo (file2)
Bottom of the inner box
Website:
@Zentrolix are designed and developed by T loft, Miami, FL 33122
Made in China
Back of the inner box
QR code (file 14)
Picture of all the cubes (file 15)
Collect them all!
Please feel free to ask as many questions as you may need to better understand the project.
NOTE: FILE 2 IS EMPTY.... PLEASE USE FILE ZenTrolix_FinalFile_10032023

```html
<!DOCTYPE html>
<html lang="en">
<head>
<meta charset="utf-8">
<title>ZenTrolix – Magnetic Fidget Pyramids Packaging</title>
<link rel="stylesheet" href="https://fonts.googleapis.com/css2?family=Montserrat:wght@600&family=Roboto+Slab:wght@400;700;900&display=swap">
<style>
  :root {
    --stage-top: #93aab5;
    --stage-bottom: #5bbcbc;
    --coral: #e8515a;
    --red: #e2474f;
    --orange: #f47a3a;
    --yellow: #f6c93a;
    --teal: #2a8f88;
    --teal-dark: #1f6660;
    --teal-ink: #1f6f68;
    --photo-teal: #7fd0d6;
    --navy: #3a4a7a;
    --purple: #8a3f9c;
    --charcoal: #2c2c2e;
    --panel: #f7f7f5;
    --side: #eeeeec;
    --ink-grey: #555a5e;
    --white: #ffffff;
  }
  * { margin: 0; padding: 0; box-sizing: border-box; }
  html, body { width: 859px; height: 1200px; overflow: hidden; }
  body { position: relative; font-family: "Roboto Slab", Georgia, serif; }

  .stage { position: absolute; left: 0; width: 859px; height: 600px; }
  .stage--front { top: 0; background: var(--stage-top); }
  .stage--back { top: 600px; background: var(--stage-bottom); }

  .view-label {
    position: absolute; top: 40px; width: 100%; text-align: center;
    font-family: "Montserrat", Arial, sans-serif; font-weight: 600;
    font-size: 32px; letter-spacing: 2px; color: var(--white);
  }

  .panel { position: absolute; top: 110px; height: 460px; overflow: hidden; }
  .panel--side { left: 204px; width: 110px; background: var(--side); border-right: 1px solid #d6d6d3; }
  .panel--face { left: 314px; width: 340px; background: var(--panel); }
  .panel__band { position: absolute; left: 0; top: 0; width: 100%; height: 14px; background: var(--coral); }

  /* Left side panel */
  .side-magnets { position: absolute; top: 26px; width: 100%; text-align: center; color: var(--red); font-weight: 900; font-size: 12px; line-height: 1.15; }
  .side-photo { position: absolute; left: 14px; top: 68px; width: 82px; height: 140px; background: linear-gradient(160deg, #9fdde0, var(--photo-teal)); }
  .side-title { position: absolute; top: 222px; width: 100%; text-align: center; }
  .side-title__main { font-size: 17px; font-weight: 900; color: var(--teal-ink); line-height: 1; }
  .side-title__sub { font-size: 8px; font-weight: 700; color: var(--red); margin-top: 3px; }
  .warning { position: absolute; left: 10px; top: 268px; width: 90px; }
  .warning__head { display: flex; align-items: center; justify-content: center; gap: 4px; height: 22px; background: var(--charcoal); color: var(--white); font-size: 10px; font-weight: 700; }
  .warning__text { margin-top: 6px; font-size: 7.5px; line-height: 1.35; color: var(--charcoal); }

  /* Right side panel */
  .included-head { position: absolute; left: 10px; top: 26px; width: 90px; padding: 6px; background: var(--navy); color: var(--white); font-size: 9px; font-weight: 700; line-height: 1.25; border-bottom: 4px solid var(--yellow); }
  .included-list { position: absolute; left: 10px; top: 88px; width: 90px; list-style: none; }
  .included-item { display: flex; align-items: center; gap: 6px; height: 58px; font-size: 8.5px; font-weight: 700; color: var(--ink-grey); line-height: 1.2; }
  .included-item__qty { flex: none; width: 24px; height: 24px; border-radius: 50%; display: flex; align-items: center; justify-content: center; color: var(--white); font-size: 10px; font-weight: 900; }
  .qty--red { background: var(--coral); }
  .qty--navy { background: var(--navy); }
  .qty--black { background: var(--charcoal); }
  .qty--purple { background: var(--purple); }
  .limitless { position: absolute; left: 10px; top: 340px; width: 90px; padding: 8px 6px; background: var(--coral); color: var(--white); font-size: 9px; font-weight: 700; line-height: 1.3; text-transform: uppercase; border-bottom: 4px solid var(--navy); }

  /* Front face */
  .front__hero {
    position: absolute; left: 0; top: 14px; width: 100%; height: 260px;
    background: radial-gradient(ellipse at 45% 0%, var(--yellow) 0%, var(--orange) 45%, var(--coral) 100%);
  }
  .front__base { position: absolute; left: 0; top: 180px; width: 100%; height: 280px; }
  .front__product {
    position: absolute; left: 100px; top: 40px; width: 150px; height: 225px;
    background: linear-gradient(160deg, #3aa79c, var(--teal-dark));
    clip-path: polygon(0 15%, 100% 15%, 75% 100%, 25% 100%);
  }
  .tagline-3d { position: absolute; right: 10px; top: 80px; width: 96px; text-align: center; color: var(--white); font-weight: 700; }
  .tagline-3d__lead { font-size: 10px; letter-spacing: .3px; }
  .tagline-3d__big { font-size: 44px; font-weight: 900; line-height: 1; color: var(--teal-ink); text-shadow: 2px 2px 0 var(--white); }
  .tagline-3d__tail { font-size: 10px; line-height: 1.3; }

  .product-name { position: absolute; left: 140px; top: 290px; }
  .product-name__main { font-size: 30px; font-weight: 900; color: var(--teal-ink); line-height: 1; }
  .product-name__sub { margin-left: 70px; margin-top: 4px; font-size: 18px; font-weight: 700; color: var(--red); line-height: 1.05; }

  .slogan-pill {
    position: absolute; right: 0; top: 368px; width: 135px; height: 32px;
    background: var(--coral); color: var(--white); font-size: 9px; line-height: 1.25;
    padding: 5px 8px; text-transform: uppercase;
  }

  .brand { position: absolute; display: flex; align-items: center; gap: 8px; }
  .brand__mark { width: 14px; height: 14px; background: var(--ink-grey); }
  .brand__name { font-size: 24px; font-weight: 400; color: var(--ink-grey); line-height: 1; }
  .front__brand { left: 150px; top: 414px; }

  /* Back face */
  .back__brand { left: 0; width: 100%; top: 110px; justify-content: center; }
  .back__brand .brand__name { font-size: 28px; }
  .back__strip {
    position: absolute; left: 0; top: 220px; width: 100%; height: 160px;
    background: linear-gradient(90deg, var(--teal) 0%, var(--teal) 60%, var(--teal-dark) 100%);
  }
  .back__tagline { position: absolute; left: 100px; top: 24px; width: 160px; text-align: center; color: var(--white); font-weight: 700; }
  .back__tagline .tagline-3d__lead { font-size: 14px; }
  .back__tagline .tagline-3d__big { font-size: 50px; color: var(--white); text-shadow: 2px 2px 0 var(--teal-dark); }
  .back__tagline .tagline-3d__tail { font-size: 14px; }
  .back__giant-3d {
    position: absolute; right: -26px; top: 42px; font-size: 92px; font-weight: 900;
    color: var(--white); transform: rotate(90deg); line-height: 1;
  }
  .back__figures { position: absolute; left: 20px; top: 394px; width: 300px; display: flex; justify-content: space-between; }
  .figure-photo { width: 66px; height: 44px; background: var(--photo-teal); border-radius: 4px; }
  .back__timeline { position: absolute; left: 20px; top: 444px; }
</style>
</head>
<body>

<section class="stage stage--front">
  <h2 class="view-label">FRONT VIEW</h2>

  <aside class="panel panel--side side-left">
    <div class="panel__band"></div>
    <div class="side-magnets">80 POWERFUL<br>MAGNETS</div>
    <div class="side-photo" role="img" aria-label="Photo of two teal magnetic pyramid pieces"></div>
    <div class="side-title">
      <div class="side-title__main">MAGNETIC</div>
      <div class="side-title__sub">FIDGET PYRAMIDS</div>
    </div>
    <div class="warning">
      <div class="warning__head">
        <svg width="11" height="10" viewBox="0 0 11 10"><polygon points="5.5,0 11,10 0,10" fill="#f6c93a"/></svg>
        WARNING
      </div>
      <p class="warning__text">Contains small magnets. Keep away from children under 3. Swallowed magnets can cause serious injury. Seek medical help at once.</p>
    </div>
  </aside>

  <div class="panel panel--face front">
    <div class="panel__band"></div>
    <div class="front__hero"></div>
    <svg class="front__base" width="340" height="280" viewBox="0 0 340 280">
      <polygon points="0,50 145,10 340,45 340,280 0,280" fill="#f7f7f5"/>
      <polyline points="0,50 145,10 340,45" fill="none" stroke="#2a8f88" stroke-width="4"/>
    </svg>
    <div class="front__product" role="img" aria-label="Product photo: teal magnetic fidget pyramids shaped into a figure with googly eyes"></div>
    <div class="tagline-3d">
      <div class="tagline-3d__lead">MAKE YOUR</div>
      <div class="tagline-3d__big">3D</div>
      <div class="tagline-3d__tail">FIGURES<br>COME TO LIFE!</div>
    </div>
    <div class="product-name">
      <div class="product-name__main">MAGNETIC</div>
      <div class="product-name__sub">FIDGET<br>PYRAMIDS</div>
    </div>
    <div class="slogan-pill">Let your creativity<br>run wild</div>
    <div class="brand front__brand">
      <span class="brand__mark"></span>
      <span class="brand__name">ZenTrolix</span>
    </div>
  </div>
</section>

<section class="stage stage--back">
  <h2 class="view-label">BACK VIEW</h2>

  <aside class="panel panel--side side-right">
    <div class="panel__band"></div>
    <div class="included-head">WHAT'S INCLUDED IN THE BOX</div>
    <ul class="included-list">
      <li class="included-item"><span class="included-item__qty qty--red">4</span>Tetrahedron pieces</li>
      <li class="included-item"><span class="included-item__qty qty--navy">16</span>Tripyramidal pieces</li>
      <li class="included-item"><span class="included-item__qty qty--black">1</span>Storage bag</li>
      <li class="included-item"><span class="included-item__qty qty--purple">1</span>Starter guide</li>
    </ul>
    <div class="limitless">Limitless designs for limitless minds</div>
  </aside>

  <div class="panel panel--face back">
    <div class="panel__band"></div>
    <div class="brand back__brand">
      <span class="brand__mark"></span>
      <span class="brand__name">ZenTrolix</span>
    </div>
    <div class="back__strip">
      <div class="back__tagline">
        <div class="tagline-3d__lead">MAKE YOUR</div>
        <div class="tagline-3d__big">3D</div>
        <div class="tagline-3d__tail">FIGURES<br>COME TO LIFE!</div>
      </div>
      <div class="back__giant-3d">3D</div>
    </div>
    <div class="back__figures">
      <div class="figure-photo" role="img" aria-label="Photo of the square figure built from magnetic pyramids"></div>
      <div class="figure-photo" role="img" aria-label="Photo of the crab figure built from magnetic pyramids"></div>
      <div class="figure-photo" role="img" aria-label="Photo of the snake figure built from magnetic pyramids"></div>
      <div class="figure-photo" role="img" aria-label="Photo of the Brickora figure built from magnetic pyramids"></div>
    </div>
    <svg class="back__timeline" width="300" height="12" viewBox="0 0 300 12">
      <line x1="0" y1="6" x2="300" y2="6" stroke="#e8515a" stroke-width="1.5"/>
      <g fill="#fff" stroke-width="2">
        <circle cx="33" cy="6" r="4" stroke="#e8515a"/>
        <circle cx="111" cy="6" r="4" stroke="#2a8f88"/>
        <circle cx="189" cy="6" r="4" stroke="#e8515a"/>
        <circle cx="267" cy="6" r="4" stroke="#2a8f88"/>
      </g>
    </svg>
  </div>
</section>

</body>
</html>
```